Marrowgate Gemworks Website revamp

Hi,

We need a working WordPress theme, not just a .PSD file. Thank you.

We need a complete revamp of our website. We sell lab grown diamonds online. We sell the idea that everyone should be able to afford a diamond. Thus our diamonds are priced very reasonably. Our selling point "the joy of giving and receiving a diamond in a little box".

Our range of products includes rings, bangles, necklace, ear rings etc. We currently only operate in Singapore. Some photos of our products are on our websites.

Need.
- Clean look and feel, simplistic preferably white and soft colours
- Easy to navigate
- No banners
- E Com
- Introduction page
- Willing to change logo if needed

Existing page: www.marrowgategemworks.com

Target Market(s)

Young ladies
Ladies
Men buying for ladies
Young boyfriends fresh out of school buying for love ones
Working ladies to match what they wear to work

Industry/Entity Type

Online

Requirements
Must have
• ECOM. Product shopping cart
Pictures uploads
Intro page
Nice to have
• Pastel colors preferred. - Color scheme is important in our business to create a long term impression. Color scheme will also be used for next potential project, i.e. packaging design.

Should not have
• Should not have old style fonts.

```html
<!DOCTYPE html>
<html lang="en">
<head>
<meta charset="utf-8">
<title>Marrowgate Gemworks</title>
<link href="https://fonts.googleapis.com/css2?family=PT+Sans:wght@400;700&display=swap" rel="stylesheet">
<style>
:root{
  --orange:#ec6a45;
  --slate:#7f9ec4;
  --ink:#3a3a3a;
  --text:#5e5e5e;
  --muted:#9a9a9a;
  --line:#e4e4e4;
  --bar:#2c2c2c;
  --hero-a:#fbf1ee;
  --hero-b:#f3ebf3;
  --hero-c:#eef2f8;
  --hero-text:#6d5f5a;
  --hero-soft:#a3948f;
}
*{box-sizing:border-box;margin:0;padding:0}
html,body{width:1200px;height:2857px;overflow:hidden}
body{position:relative;background:#fff;font-family:"PT Sans",Arial,sans-serif;color:var(--text)}
.abs{position:absolute}
a{color:inherit}

.top-bar{left:0;top:0;width:1200px;height:31px;background:var(--bar)}
.top-bar .links{position:absolute;right:38px;top:8px;font-size:12px;color:#ddd;display:flex;gap:38px}

.logo{left:48px;top:76px;width:250px;display:flex;align-items:center;gap:10px;font-size:20px;color:var(--ink);white-space:nowrap}
.logo .mark{width:18px;height:18px;border:2px solid var(--ink);flex:none}
.welcome{left:310px;top:80px;font-size:14px;color:var(--ink)}
.welcome a{text-decoration:underline}
.search{left:800px;top:64px;width:210px;height:42px;border-radius:21px;background:#f1f1f1;font-size:14px;color:#aaa;padding:11px 18px}
.search-btn{left:994px;top:63px;width:44px;height:44px;border-radius:50%;background:var(--slate)}
.cart-btn{left:1048px;top:63px;width:44px;height:44px;border-radius:50%;background:var(--orange)}
.cart-label{left:1100px;top:75px;font-size:15px;font-weight:700;color:var(--ink)}
.nav-rule{left:310px;top:140px;width:870px;height:1px;background:var(--line)}
.main-nav{left:310px;top:160px;display:flex;gap:38px;font-size:17px;font-weight:700;color:var(--ink);letter-spacing:.4px}

.hero{left:0;top:238px;width:1200px;height:432px;background:linear-gradient(100deg,var(--hero-a),var(--hero-b) 55%,var(--hero-c))}
.hero-photo{left:470px;top:278px;width:230px;height:360px;border-radius:10px;background:radial-gradient(ellipse at 50% 45%,#ffffff,#d8d4da 55%,rgba(243,235,243,0) 75%)}
.hero-point{font-size:12px;letter-spacing:1px;color:var(--hero-soft);text-align:right;line-height:1.4}
.hero-point b{color:var(--hero-text)}
.hero-point .dash{position:absolute;top:10px;left:150px;width:80px;border-top:1px dashed #c9bcb7}
.hero-title{left:752px;top:330px;font-size:30px;color:var(--hero-text);letter-spacing:1px}
.hero-copy{left:752px;top:400px;width:400px;font-size:15px;line-height:1.55;color:var(--hero-text)}
.btn-buy{left:752px;top:497px;width:134px;height:46px;border-radius:23px;background:var(--orange);color:#fff;font-size:14px;font-weight:700;text-align:center;line-height:46px}

.perks{left:0;top:770px;width:1200px;height:122px;background:#fafafa}
.perk{display:flex;align-items:center;gap:18px;font-size:20px;color:var(--ink);position:absolute;top:32px}
.perk .dot{width:64px;height:64px;border-radius:50%;flex:none;display:flex;align-items:center;justify-content:center}
.perk b{font-weight:700}

.section-title{left:19px;top:956px;font-size:22px;color:var(--ink);letter-spacing:.5px}
.section-rule{left:19px;top:1005px;width:1162px;height:1px;background:var(--line)}

.product{width:270px;height:404px;background:#fff;border:1px solid #ececec;box-shadow:0 1px 4px rgba(0,0,0,.08);overflow:hidden}
.product.active{box-shadow:0 3px 12px rgba(0,0,0,.16)}
.product .photo{position:absolute;left:25px;top:24px;width:220px;height:210px;border-radius:6px;background:radial-gradient(circle,#e3e3e6,#fff 72%)}
.product .name{position:absolute;left:0;right:0;top:272px;text-align:center;font-size:17px;color:var(--ink);letter-spacing:.5px}
.product .rule{position:absolute;left:24px;right:24px;top:320px;height:1px;background:var(--line)}
.product .plus{position:absolute;left:129px;top:309px;width:12px;height:22px;background:#fff;text-align:center;font-size:13px;color:#bbb}
.product .price{position:absolute;left:0;right:0;top:350px;text-align:center;font-size:18px;color:var(--orange)}
.product .was{position:absolute;left:0;right:0;top:375px;text-align:center;font-size:14px;color:var(--muted);text-decoration:line-through}
.product.active .price{text-align:left;left:24px}
.product .compare{position:absolute;left:175px;top:353px;font-size:18px;color:#aaa}
.product .add{position:absolute;left:204px;top:340px;width:44px;height:44px;border-radius:50%;background:var(--orange)}
.sale{position:absolute;left:0;top:0}

.about{width:566px;height:420px;border:1px solid #ececec;background:#fcfcfc;padding:20px 24px}
.about h3{font-size:20px;font-weight:400;color:var(--ink);margin-bottom:30px}
.about p{font-size:14.5px;line-height:1.6;margin-bottom:24px;color:#555}

.footer{left:0;top:2440px;width:1200px;height:417px;background:#f7f7f7}
.foot-col h4{font-size:18px;font-weight:400;color:var(--ink);letter-spacing:.5px;margin-bottom:30px}
.foot-col li{list-style:none;font-size:14px;color:#555;line-height:30px}
.foot-rule{left:0;top:2736px;width:1200px;height:1px;background:#e2e2e2}
.contact-line{display:flex;gap:12px;font-size:14px;line-height:20px;margin-bottom:10px;color:#555}
.contact-line svg{flex:none;margin-top:3px}
.newsletter{left:24px;top:2758px;display:flex;align-items:center;gap:14px}
.newsletter .dot{width:48px;height:48px;border-radius:50%;background:var(--orange)}
.newsletter span{font-size:19px;color:var(--ink)}
.news-note{left:207px;top:2773px;width:360px;font-size:13px;color:#555;white-space:nowrap}
.news-field{left:580px;top:2760px;width:272px;height:44px;border-radius:22px;border:1px solid #ddd;background:#fff;font-size:13px;color:#888;padding:12px 22px}
.pay{top:2766px;width:62px;height:36px;border-radius:4px;border:1px solid #ddd;background:#fff}
.pay i{position:absolute;left:13px;top:11px;width:34px;height:12px;border-radius:2px}
</style>
</head>
<body>

<div class="abs top-bar"><div class="links"><span>My Account</span><span>Contact Us</span></div></div>

<div class="abs logo"><span class="mark"></span><span>Marrowgate Gemworks</span></div>
<div class="abs welcome">Welcome visitor you can <a>login</a> or <a>create an account</a>.</div>
<div class="abs search">Search</div>
<div class="abs search-btn"><svg width="44" height="44" viewBox="0 0 44 44"><circle cx="20" cy="20" r="6" fill="none" stroke="#fff" stroke-width="2"/><line x1="24.5" y1="24.5" x2="29" y2="29" stroke="#fff" stroke-width="2"/></svg></div>
<div class="abs cart-btn"><svg width="44" height="44" viewBox="0 0 44 44"><path d="M14 17h3l3 10h9l2-7H18" fill="none" stroke="#fff" stroke-width="2"/><circle cx="21" cy="30" r="1.5" fill="#fff"/><circle cx="28" cy="30" r="1.5" fill="#fff"/></svg></div>
<div class="abs cart-label">CART £0</div>
<div class="abs nav-rule"></div>
<nav class="abs main-nav"><span>HOME</span><span>OUR STORY</span><span>OUR DIAMONDS</span><span>SHOP</span><span>CONTACT US</span></nav>

<section class="abs hero"></section>
<div class="abs hero-photo" role="img" aria-label="Photo of two diamond engagement rings with amber centre stones"></div>
<div class="abs hero-point" style="left:150px;top:318px;width:232px"><div style="width:140px">REAL BEAUTIFUL<br><b>DIAMOND</b></div><span class="dash"></span></div>
<div class="abs hero-point" style="left:150px;top:418px;width:232px"><div style="width:140px">INTERSPERSED<br><b>WITH WHITE GOLD</b></div><span class="dash"></span></div>
<div class="abs hero-point" style="left:150px;top:552px;width:232px"><div style="width:140px">HANDMADE<br><b>FINEST JEWELERS</b></div><span class="dash"></span></div>
<div class="abs hero-title">ENGAGEMENT RINGS</div>
<p class="abs hero-copy">The hardest part is over – you've found the love of your life. Now is the time to find the perfect diamond engagement ring and plan a beautiful proposal.</p>
<div class="abs btn-buy">BUY NOW</div>

<section class="abs perks">
  <div class="perk" style="left:19px"><span class="dot" style="background:var(--orange)"><svg width="30" height="30" viewBox="0 0 30 30"><path d="M4 15l11-11h10v10L14 25z" fill="none" stroke="#fff" stroke-width="2.4"/><circle cx="20" cy="10" r="2" fill="#fff"/></svg></span><span><b>INSANE DISCOUNTS</b> ON NEW COLLECTION!</span></div>
  <div class="perk" style="left:607px"><span class="dot" style="background:var(--slate)"><svg width="32" height="32" viewBox="0 0 32 32"><rect x="8" y="4" width="16" height="20" rx="3" fill="none" stroke="#fff" stroke-width="2.4"/><line x1="8" y1="14" x2="24" y2="14" stroke="#fff" stroke-width="2"/><circle cx="12" cy="27" r="2" fill="#fff"/><circle cx="20" cy="27" r="2" fill="#fff"/></svg></span><span><b>FREE SHIPPING</b> ON ORDERS OVER $500</span></div>
</section>

<h2 class="abs section-title">FEATURED PRODUCTS</h2>
<div class="abs section-rule"></div>

<div class="abs product" style="left:21px;top:1093px">
  <div class="photo" role="img" aria-label="Diamond tennis bracelet"></div>
  <svg class="sale" width="80" height="80" viewBox="0 0 80 80"><path d="M0 0h52L0 52z" fill="var(--orange)"/><text x="14" y="30" transform="rotate(-45 20 26)" fill="#fff" font-size="12" font-weight="700" font-family="PT Sans, sans-serif">SALE</text></svg>
  <div class="name">BANGS</div><div class="rule"></div><div class="plus">+</div>
  <div class="price" style="top:342px">£19.99</div><div class="was">£25.07</div>
</div>
<div class="abs product" style="left:314px;top:1093px">
  <div class="photo" role="img" aria-label="Pair of diamond drop earrings"></div>
  <div class="name">DROP</div><div class="rule"></div><div class="plus">+</div><div class="price">£38.87</div>
</div>
<div class="abs product active" style="left:612px;top:1093px">
  <div class="photo" role="img" aria-label="Eternity ring set with violet centre stone"></div>
  <div class="name">ETERNITY</div><div class="rule"></div><div class="plus">+</div><div class="price">£87.19</div>
  <div class="compare">⇄</div>
  <div class="add"><svg width="44" height="44" viewBox="0 0 44 44"><path d="M14 17h3l3 10h9l2-7H18" fill="none" stroke="#fff" stroke-width="2"/><circle cx="21" cy="30" r="1.5" fill="#fff"/><circle cx="28" cy="30" r="1.5" fill="#fff"/></svg></div>
</div>
<div class="abs product" style="left:912px;top:1093px">
  <div class="photo" role="img" aria-label="Crossover diamond bangle"></div>
  <div class="name">KRIS</div><div class="rule"></div><div class="plus">+</div><div class="price">£38.87</div>
</div>

<div class="abs product" style="left:21px;top:1529px">
  <div class="photo" role="img" aria-label="Ring with sapphire centre stone and diamond band"></div>
  <div class="name">ETERNITY</div><div class="rule"></div><div class="plus">+</div><div class="price">£31.96</div>
</div>
<div class="abs product" style="left:314px;top:1529px">
  <div class="photo" role="img" aria-label="Vintage style diamond band"></div>
  <div class="name">PINK</div><div class="rule"></div><div class="plus">+</div><div class="price">£31.96</div>
</div>
<div class="abs product" style="left:612px;top:1529px">
  <div class="photo" role="img" aria-label="Halo diamond engagement ring"></div>
  <div class="name">THE ONE</div><div class="rule"></div><div class="plus">+</div><div class="price">£31.96</div>
</div>
<div class="abs product" style="left:912px;top:1529px">
  <div class="photo" role="img" aria-label="Stacked gold, rose and white gold rings"></div>
  <div class="name">SOUL OF AN ANGEL</div><div class="rule"></div><div class="plus">+</div><div class="price">£38.87</div>
</div>

<section class="abs about" style="left:21px;top:1957px">
  <h3>ABOUT US</h3>
  <p>«Larkmoor» company became famous among thousands of visitors and purchasers of the most known online resource copyright works during the short period of its existence.</p>
  <p>«Larkmoor» offers a number of creative products such as: online stores templates, one page promo sites, graphic works and corporate style for the wide audience. The company owes its success to the friendly team of professionals, who create exclusive designs, unique and clear functionality of the templates.</p>
  <p>Corporate style and graphic works always have the perfect design so you do not have to change a lot of settings to achieve the desired style.</p>
</section>
<section class="abs about" style="left:612px;top:1957px">
  <h3>ABOUT US</h3>
  <p>«Larkmoor» company became famous among thousands of visitors and purchasers of the most known online resource copyright works during the short period of its existence.</p>
  <p>«Larkmoor» offers a number of creative products such as: online stores templates, one page promo sites, graphic works and corporate style for the wide audience. The company owes its success to the friendly team of professionals, who create exclusive designs, unique and clear functionality of the templates.</p>
  <p>Corporate style and graphic works always have the perfect design so you do not have to change a lot of settings to achieve the desired style.</p>
</section>

<footer class="abs footer"></footer>
<div class="abs foot-col" style="left:24px;top:2525px;width:270px">
  <h4>CONTACT US</h4>
  <div class="contact-line"><svg width="12" height="16" viewBox="0 0 12 16"><path d="M6 0a6 6 0 0 1 6 6c0 4-6 10-6 10S0 10 0 6a6 6 0 0 1 6-6z" fill="var(--slate)"/><circle cx="6" cy="6" r="2" fill="#fff"/></svg><span>27 Fernhollow Road,<br>#03-12 Quayside Court,<br>Singapore 500123</span></div>
  <div class="contact-line"><svg width="14" height="14" viewBox="0 0 14 14"><path d="M3 0l3 3-2 2c1 2 3 4 5 5l2-2 3 3-2 3C6 14 0 8 0 2z" fill="var(--slate)"/></svg><span>+65 9000 4417</span></div>
  <div class="contact-line"><svg width="14" height="12" viewBox="0 0 14 12"><rect x="0" y="1" width="14" height="10" rx="1" fill="var(--slate)"/><path d="M1 2l6 5 6-5" fill="none" stroke="#fff" stroke-width="1.3"/></svg><span>info@marrowgategemworks.com</span></div>
</div>
<div class="abs foot-col" style="left:317px;top:2525px"><h4>INFORMATION</h4><ul><li>Sample Page</li><li>Contact Us</li><li>News</li></ul></div>
<div class="abs foot-col" style="left:614px;top:2525px"><h4>CUSTOMER SERVICE</h4><ul><li>Checkout</li><li>Cart</li><li>Privacy Policy</li></ul></div>
<div class="abs foot-col" style="left:910px;top:2525px"><h4>MY ACCOUNT</h4><ul><li>My Account</li><li>Edit My Address</li><li>Logout</li><li>Lost Password</li></ul></div>
<div class="abs foot-rule"></div>
<div class="abs newsletter"><span class="dot"></span><span>Newsletter</span></div>
<div class="abs news-note">Subscribe to notifications about discounts from our store</div>
<div class="abs news-field">Email<svg style="position:absolute;right:18px;top:14px" width="10" height="16" viewBox="0 0 10 16"><path d="M2 2l6 6-6 6" fill="none" stroke="#555" stroke-width="2"/></svg></div>
<div class="abs pay" style="left:912px"><i style="background:#d7dce8"></i></div>
<div class="abs pay" style="left:982px"><i style="background:#d5e3ee"></i></div>
<div class="abs pay" style="left:1052px"><i style="background:#f0dccf"></i></div>
<div class="abs pay" style="left:1122px"><i style="background:#e8e0d4"></i></div>

</body>
</html>
```